Modern Business Card Design Needed for Young Realtor

Information that is going on the card:Marvin Pold
Broker/Owner
555.210.3367
Marvin@MPoldRealty.com
www.MPoldRealty.com

Would also like to include my Instagram Handle somewhere. Probably on the back: the_queencity_realtorMy previous business card is attached, I like that one but would like an updated version and maybe a few design changes

Marvin Pold
Broker/Owner
555.210.3367
Marvin@MPoldRealty.com
www.MPoldRealty.com

• Would also like to include my Instagram Handle somewhere. Probably on the back: the_pinecrest_realtor
• Dorrance Hale or the DH (logo from the previous card.)

```html
<!DOCTYPE html>
<html lang="en">
<head>
<meta charset="utf-8">
<title>MPold Realty – Business Card</title>
<link rel="stylesheet" href="https://fonts.googleapis.com/css2?family=Tinos:wght@400&display=swap">
<style>
  :root {
    --bg: #6e6c69;
    --card-white: #ffffff;
    --brand-red: #b52132;
    --brand-red-dark: #9e1b2b;
    --ink: #2a2a2a;
    --photo-green: #7d9a5c;
    --photo-stone: #b9b3a6;
  }
  * { margin: 0; padding: 0; box-sizing: border-box; }
  html, body {
    width: 1200px; height: 856px; overflow: hidden;
    background: var(--bg);
  }
  .canvas {
    width: 1200px; height: 856px;
    display: flex; align-items: center; justify-content: center; gap: 60px;
  }
  .card {
    width: 520px; height: 298px;
    border-radius: 26px;
    overflow: hidden;
    position: relative;
    box-shadow: 0 10px 24px rgba(0,0,0,.25);
  }

  /* Front */
  .card-front { background: var(--card-white); display: flex; }
  .front-info {
    width: 47%;
    display: flex; flex-direction: column; align-items: center;
    padding-top: 62px;
    font-family: "Tinos", serif;
    color: var(--ink);
  }
  .divider { width: 5px; background: var(--brand-red); }
  .front-photo {
    flex: 1;
    background: linear-gradient(160deg, var(--photo-green) 0%, var(--photo-stone) 55%, #5d5f62 100%);
  }
  .brand-name {
    font-family: "Tinos", serif;
    font-size: 24px;
    font-weight: 400;
    color: var(--brand-red);
    white-space: nowrap;
  }
  .agent-name {
    margin-top: 26px;
    font-size: 20px;
    font-weight: 400;
    letter-spacing: .5px;
    text-transform: uppercase;
  }
  .agent-name .first { color: var(--brand-red); }
  .agent-title { font-size: 14px; margin-top: 2px; }
  .contact {
    margin-top: 14px;
    list-style: none;
    text-align: center;
    font-size: 14px;
    line-height: 1.35;
  }
  .contact .accent { color: var(--brand-red); }

  /* Back */
  .card-back {
    background: linear-gradient(180deg, var(--brand-red) 0%, var(--brand-red-dark) 100%);
    display: flex; flex-direction: column; align-items: flex-end; justify-content: center;
    padding: 0 44px 0 0;
    color: #fff;
    font-family: "Tinos", serif;
  }
  .back-brand {
    font-size: 30px;
    font-weight: 400;
    color: #fff;
    margin-top: 50px;
  }
  .handle {
    font-size: 14px;
    margin-top: 8px;
  }
</style>
</head>
<body>
  <main class="canvas">
    <section class="card card-front">
      <div class="front-info">
        <div class="brand-name">MPold Realty</div>
        <h1 class="agent-name"><span class="first">Marvin</span> Pold</h1>
        <p class="agent-title">Broker/Owner</p>
        <ul class="contact">
          <li>555.210.3367</li>
          <li>Marvin@MPoldRealty.com</li>
          <li>www.<span class="accent">MPoldRealty</span>.com</li>
        </ul>
      </div>
      <div class="divider"></div>
      <div class="front-photo" role="img" aria-label="Portrait photo of the broker outdoors in a grey blazer"></div>
    </section>

    <section class="card card-back">
      <div class="back-brand">MPold Realty</div>
      <p class="handle">the_pinecrest_realtor</p>
    </section>
  </main>
</body>
</html>
```